Local fast-growing company in the service sector

We are looking for a modern business card design, which should also appear on our letterheads

Target Market(s)

Private and industrial sectors

Contact Information for Business Card

Vorname Name
Kellbacher Str. 38
74819 Talweiler
Tel.: 07162-418395-0
Name@service-tkwl.de

Colors
9d9d9d
919191
aaaaaa

Requirements
Must have
• The logo (file) in silver

```html
<!DOCTYPE html>
<html lang="de">
<head>
<meta charset="utf-8">
<title>TKWL Visitenkarte</title>
<link rel="stylesheet" href="https://fonts.googleapis.com/css2?family=Open+Sans:wght@400;700&display=swap">
<style>
  :root {
    --backdrop: #2b2b2b;
    --paper: #ffffff;
    --silver: #9d9d9d;
    --silver-mid: #919191;
    --silver-light: #aaaaaa;
    --rule: #c4c4c4;
    --ink: #3a3a3a;
    --band-dark: #5a5a5a;
  }
  * { margin: 0; padding: 0; box-sizing: border-box; }
  html, body { width: 1200px; height: 716px; overflow: hidden; }
  body {
    background: var(--backdrop);
    font-family: "Open Sans", Arial, sans-serif;
    position: relative;
  }
  .card {
    position: absolute;
    top: 190px;
    width: 520px;
    height: 336px;
    background: var(--paper);
    overflow: hidden;
  }
  .card--front { left: 50px; }
  .card--back { left: 630px; }

  .brand {
    position: absolute;
    display: flex;
    align-items: center;
    gap: 8px;
    color: var(--silver);
    font-weight: 700;
    letter-spacing: 1px;
  }
  .brand__mark {
    width: 18px;
    height: 18px;
    background: var(--silver);
  }
  .card--front .brand { left: 34px; top: 26px; font-size: 34px; line-height: 1.3; }
  .card--front .brand-web {
    position: absolute;
    left: 60px; top: 72px;
    font-size: 15px;
    color: var(--silver);
    font-weight: 700;
  }

  .holder {
    position: absolute;
    left: 34px; top: 104px;
    font-size: 20px;
    font-weight: 700;
    color: var(--ink);
  }
  .holder-rule {
    position: absolute;
    left: 34px; top: 138px;
    width: 300px; height: 1px;
    background: var(--rule);
  }

  .contact {
    position: absolute;
    left: 250px; top: 196px;
    list-style: none;
    font-size: 13px;
    color: var(--ink);
    line-height: 22px;
  }
  .contact li { display: flex; align-items: center; gap: 6px; white-space: nowrap; }
  .contact svg { width: 12px; height: 12px; flex: none; }
  .contact-rule {
    position: absolute;
    left: 250px; top: 272px;
    width: 240px; height: 1px;
    background: var(--rule);
  }

  .band {
    position: absolute;
    bottom: 0; height: 10px;
  }
  .band--light { left: 0; width: 200px; background: var(--silver-light); }
  .band--dark { left: 200px; width: 320px; background: var(--band-dark); }

  .card--back .lockup {
    position: absolute;
    left: 0; right: 0; top: 118px;
    display: flex;
    flex-direction: column;
    align-items: center;
  }
  .card--back .brand { position: static; font-size: 56px; line-height: 1; }
  .card--back .brand__mark { width: 26px; height: 26px; }
  .card--back .brand-web {
    margin-top: 6px;
    font-size: 22px;
    font-weight: 700;
    color: var(--silver);
    letter-spacing: 1px;
  }
</style>
</head>
<body>
  <section class="card card--front" aria-label="Vorderseite">
    <div class="brand"><span class="brand__mark"></span>TKWL</div>
    <div class="brand-web">service-tkwl.de</div>

    <div class="holder">Vorname Name</div>
    <div class="holder-rule"></div>

    <ul class="contact">
      <li>
        <svg viewBox="0 0 12 12" aria-hidden="true"><circle cx="6" cy="6" r="6" fill="#919191"/><path d="M4 3.2c.4 0 .6.9.4 1.2-.2.3.8 1.6 1.2 1.8.3.2.6-.1.9 0 .3.2.9.6.7 1-.3.5-.9.7-1.4.5C4.4 7.2 3.3 5.6 3.3 4.3c0-.6.3-1.1.7-1.1z" fill="#fff"/></svg>
        07162-418395-0
      </li>
      <li>
        <svg viewBox="0 0 12 12" aria-hidden="true"><circle cx="6" cy="6" r="6" fill="#919191"/><rect x="3" y="4" width="6" height="4" fill="#fff"/><path d="M3 4l3 2.2L9 4" stroke="#919191" stroke-width=".7" fill="none"/></svg>
        Name@service-tkwl.de
      </li>
      <li>
        <svg viewBox="0 0 12 12" aria-hidden="true"><circle cx="6" cy="6" r="6" fill="#919191"/><path d="M6 2.6a2 2 0 0 1 2 2c0 1.5-2 4-2 4s-2-2.5-2-4a2 2 0 0 1 2-2z" fill="#fff"/><circle cx="6" cy="4.6" r=".7" fill="#919191"/></svg>
        Kellbacher Str. 38, 74819 Talweiler
      </li>
    </ul>
    <div class="contact-rule"></div>

    <div class="band band--light"></div>
    <div class="band band--dark"></div>
  </section>

  <section class="card card--back" aria-label="Rückseite">
    <div class="lockup">
      <div class="brand"><span class="brand__mark"></span>TKWL</div>
      <div class="brand-web">service-tkwl.de</div>
    </div>
  </section>
</body>
</html>
```